依頼詳細
色の指定はありませんが、円満相続をイメージさせる明るい色を希望します。
お客様へのわかりやすさ、相談したいなと思わせるイメージです。
記載項目
表面:氏名/森岡達彦(モリオカタツヒコ)会社名/有限会社ミナレスト 役職/代表取締役 資格/不動産賃貸経営管理士・宅地建物取引主任者・相続士・NPO法人継承くらし支援ネット会員
住所/〒798-0417愛媛県宇和島市柳川町3丁目4-2 電話/0895-41-7782 Fax/0895-41-7783 携帯/090-5827-1146 Mail/morioka@minarest-ex.jp http://www.minarest-ex.jp

裏面:社是・・・創動継志       創造・行動・継続   習
(※添付しているロゴ使用)    志       慣
※志を分母、創造・行動・継続を分子、上に線を入れられなかったので文字で説明しまし
た。上記を習慣にしていくという意味です。

理念・・・志事(シゴト)を通じ、物心両面の幸福を追求し、自らが創造成長することで、
縁ある大事な方々に、喜んでもらえることを使命とします。

※上記に「相続を受ける人によって様々な方法や対策があります。自身の相続や不動産業・生   保・損保代理店の経験に基づいたお客様にとって最善な方法をご提案します。」みたいなわか
りやすい説明をいれて欲しいです。

希望イメージ
シンプル 複雑
単色 カラフル
暗い 明るい
日常 高級
遊び心 厳粛
未来的 伝統的
女性的 男性的
希望する色
納品ファイル
• 高解像度JPG (.jpg)
• イラストレーター形式 (.ai)
補足説明
依頼公開後の追記内容

明るく、もらった方に安心感を与えられるような点

貴重なお時間をいただき、また素敵なご提案をいただきましてありがとうございました。

```html
<!DOCTYPE html>
<html lang="ja">
<head>
<meta charset="utf-8">
<title>名刺 表面 — 有限会社ミナレスト</title>
<link rel="stylesheet" href="https://fonts.googleapis.com/css2?family=Noto+Sans+JP:wght@400;500;700&family=Noto+Serif:wght@400&display=swap">
<style>
  :root {
    --green: #2f9a5b;
    --green-pale: #e5eed6;
    --green-mark: #cfe0bc;
    --ink: #2a2a2a;
    --ink-soft: #4a4a4a;
    --white: #ffffff;
  }
  html, body {
    margin: 0;
    padding: 0;
    width: 882px;
    height: 1200px;
    overflow: hidden;
    background: var(--white);
  }
  .card {
    position: relative;
    width: 882px;
    height: 1200px;
    background: var(--white);
    font-family: "Noto Sans JP", sans-serif;
    color: var(--ink);
  }
  .card__header {
    position: absolute;
    left: 0; top: 0;
    width: 882px;
    height: 440px;
    background: var(--green-pale);
  }
  .brand {
    position: absolute;
    left: 91px;
    top: 70px;
    display: flex;
    align-items: center;
    gap: 16px;
  }
  .brand__square {
    width: 40px;
    height: 40px;
    background: var(--green);
  }
  .brand__name {
    margin: 0;
    font-size: 48px;
    font-weight: 500;
    line-height: 1;
    color: var(--green);
  }
  .header-illustration {
    position: absolute;
    left: 560px;
    top: 190px;
    width: 230px;
    height: 170px;
    border-radius: 8px;
    background: var(--green-mark);
  }
  .person {
    position: absolute;
    left: 91px;
    top: 560px;
  }
  .person__title {
    margin: 0;
    font-size: 30px;
    line-height: 1;
  }
  .person__name {
    margin: 18px 0 0;
    font-size: 68px;
    font-weight: 500;
    line-height: 1;
    letter-spacing: 4px;
  }
  .person__roman {
    font-family: "Noto Serif", serif;
    font-size: 30px;
    font-weight: 400;
    letter-spacing: 0;
    margin-left: 14px;
  }
  .person__mobile {
    margin: 18px 0 0;
    font-size: 30px;
    line-height: 1;
  }
  .person__licenses {
    margin: 28px 0 0;
    font-size: 24px;
    line-height: 1.4;
    color: var(--ink-soft);
  }
  .company {
    position: absolute;
    left: 91px;
    top: 870px;
  }
  .company__name {
    margin: 0;
    font-size: 42px;
    font-weight: 700;
    color: var(--green);
    line-height: 1;
  }
  .company__contact {
    margin: 16px 0 0;
    font-size: 28px;
    line-height: 1.35;
    color: var(--ink-soft);
  }
  .card__footer {
    position: absolute;
    left: 0; bottom: 0;
    width: 882px;
    height: 92px;
    background: var(--green);
    display: flex;
    align-items: center;
    justify-content: center;
  }
  .site-url {
    color: var(--white);
    font-size: 44px;
    font-weight: 500;
    letter-spacing: 1px;
  }
</style>
</head>
<body>
  <article class="card">
    <header class="card__header">
      <div class="brand">
        <span class="brand__square" aria-hidden="true"></span>
        <p class="brand__name">MINAREST</p>
      </div>
      <div class="header-illustration" role="img" aria-label="手のひらに家をのせたイラスト"></div>
    </header>

    <section class="person">
      <p class="person__title">代表取締役</p>
      <h1 class="person__name">森岡 達彦<span class="person__roman">Tatsuhiko Morioka</span></h1>
      <p class="person__mobile">Mobile : 090-5827-1146</p>
      <p class="person__licenses">不動産賃貸経営管理士・宅地建物取引主任者<br>相続士・NPO法人継承くらし支援ネット会員</p>
    </section>

    <section class="company">
      <h2 class="company__name">有限会社ミナレスト</h2>
      <p class="company__contact">〒798-0417 愛媛県宇和島市柳川町3丁目4-2<br>Tel : 0895-41-7782　Fax : 0895-41-7783<br>E-mail : morioka@minarest-ex.jp</p>
    </section>

    <footer class="card__footer">
      <span class="site-url">http://www.minarest-ex.jp</span>
    </footer>
  </article>
</body>
</html>
```